Crooked Thrill

I would like a website that does e-commerce and able to take payments for merchandise and orders.

Target Market(s)

Skate, BMX, surf, drink, adventure, motorcycle, rock n roll, bars, hot rods, tattoos, rebels

Industry/Entity Type

Brand market

Coding

Coded - Design and coding required

Number of Pages Required

1 page

Font styles to use
Serif

Requirements
Must have
• E-commerce
Nice to have
• Pictures of merch on people... Ex. People wearing our hats

```html
<!DOCTYPE html>
<html lang="en">
<head>
<meta charset="utf-8">
<title>Crooked Thrill</title>
<link href="https://fonts.googleapis.com/css2?family=Montserrat:ital,wght@0,300;0,400;0,500;0,600;0,700;0,800;1,400&family=Raleway:wght@300;400&family=Roboto:wght@700&display=swap" rel="stylesheet">
<style>
:root{
  --ink:#1f1e25;
  --text:#333;
  --muted:#8a8a8a;
  --accent:#e9513a;
  --deep-red:#d4231b;
  --band-a:#ea5d4c;
  --band-b:#f07d77;
  --line:#d9d9d9;
  --paper:#fff;
  --green:#00b67a;
}
*{margin:0;padding:0;box-sizing:border-box}
html,body{width:1200px;height:2984px;overflow:hidden;background:var(--paper)}
body{position:relative;font-family:'Montserrat',sans-serif;color:var(--text)}
.abs{position:absolute}

/* header */
.site-header{position:absolute;left:0;top:0;width:1200px;height:69px;background:var(--ink)}
.menu-icon{left:145px;top:25px;width:24px;height:18px}
.menu-icon span{display:block;height:3px;background:#fff;margin-bottom:4.5px}
.brand-badge{left:179px;top:4px;width:100px;height:100px;border-radius:50%;background:#fff;border:3px solid var(--ink);z-index:5;display:flex;align-items:center;justify-content:center;text-align:center;font-weight:700;font-size:13px;line-height:1.2;color:var(--ink)}
.search-icon{left:797px;top:24px}
.sign-in{left:881px;top:29px;color:#fff;font-size:10px;font-weight:600;letter-spacing:.3px}
.cart-icon{left:1013px;top:21px}
.cart-count{left:1030px;top:37px;width:15px;height:15px;border-radius:50%;background:var(--accent);color:#fff;font-size:8px;text-align:center;line-height:15px}
.cart-label{left:1057px;top:20px;font-size:9px;color:#666}
.cart-total{left:1057px;top:35px;font-size:11px;color:#fff;font-weight:700}

/* hero */
.hero{position:absolute;left:0;top:69px;width:1200px;height:596px;background:linear-gradient(90deg,#d9d9db 0%,#ececee 55%,#f7f7f8 100%)}
.hero-photo{position:absolute;left:0;top:0;width:640px;height:596px;background:linear-gradient(180deg,#cfcfd2 0%,#e4e4e6 45%,#2a2a2c 88%,#1a1a1c 100%)}
.deal-kicker{left:670px;top:182px;font-family:'Raleway',sans-serif;font-weight:300;font-size:32px;color:#333;letter-spacing:.5px}
.deal-kicker::after{content:"";display:inline-block;width:58px;height:1px;background:#444;vertical-align:middle;margin-left:14px}
.deal-title{left:670px;top:232px;font-weight:800;font-size:53px;color:#111;letter-spacing:-.5px}
.deal-price{left:670px;top:295px;font-weight:700;font-size:31px;color:#111}
.deal-bought{left:675px;top:348px;font-size:16px;font-weight:600;letter-spacing:3.5px;color:#111;display:flex;align-items:center;gap:14px}
.countdown{left:675px;top:408px;display:flex;gap:12px}
.count-box{width:78px;height:76px;background:#fff;box-shadow:0 2px 6px rgba(0,0,0,.08);text-align:center;padding-top:10px}
.count-box b{display:block;font-size:26px;font-weight:700;color:#111}
.count-box span{font-size:11px;color:#888}
.btn-accent{height:35px;background:var(--accent);color:#fff;font-size:12px;font-weight:700;letter-spacing:2.5px;display:flex;align-items:center;justify-content:center}
.shop-now{left:677px;top:521px;width:158px}
.view-details{left:847px;top:521px;width:158px}

/* about */
.about{left:111px;top:698px;width:960px;font-size:17.5px;line-height:22.5px;color:#333}

/* sections */
.section-title{font-family:'Raleway',sans-serif;font-weight:300;font-size:32px;color:#222}
.product-row{left:116px;display:flex;gap:25px}
.product-card{width:177px}
.product-image{width:176px;height:174px}
.product-name{font-size:15px;margin-top:19px;margin-left:2px;color:#222}
.product-specs{font-size:10px;line-height:15px;color:var(--muted);margin:6px 0 0 2px}
.product-price{display:flex;align-items:center;font-size:12.5px;margin:8px 0 0 2px}
.product-price s{color:var(--deep-red);margin-right:9px}
.product-price b{font-weight:500;color:#111}
.likes{margin-left:auto;font-size:10px;color:var(--muted);display:flex;align-items:center;gap:3px}
.free-ship{font-size:9px;font-style:italic;color:var(--muted);margin:7px 0 0 2px}
.detail-btn{margin-top:10px;height:34px;border:1px solid #bbb;font-size:12px;letter-spacing:2.5px;color:#888;display:flex;align-items:center;justify-content:center}
.carousel-arrow{width:35px;height:35px;border-radius:50%;display:flex;align-items:center;justify-content:center}
.arrow-left{background:#ddd}
.arrow-right{background:#555}

/* signup */
.signup{position:absolute;left:0;top:1327px;width:1200px;height:306px;background:linear-gradient(90deg,var(--band-a),var(--band-b));overflow:hidden}
.signup-arc{position:absolute;left:105px;top:40px;width:1300px;height:700px;border-radius:50%;background:rgba(255,255,255,.05)}
.signup h2{position:absolute;left:0;width:1200px;top:68px;text-align:center;font-weight:400;font-size:39px;color:#fff}
.signup p{position:absolute;left:0;width:1200px;top:134px;text-align:center;font-size:16.5px;color:#fff}
.signup-form{position:absolute;left:266px;top:181px;width:670px;height:39px;display:flex}
.email-field{flex:1;background:#fff;font-size:11px;letter-spacing:2px;color:#ccc;padding:14px 0 0 38px}
.subscribe{width:159px;background:var(--deep-red);color:#fff;font-size:12px;font-weight:700;letter-spacing:2.5px;display:flex;align-items:center;justify-content:center}
.dot-grid{position:absolute;left:1073px;top:133px}

/* reviews */
.review-card{position:absolute;top:1810px;width:292px;height:234px;background:#fff;box-shadow:0 3px 14px rgba(0,0,0,.08);padding:26px 24px 0}
.review-quote{position:absolute;right:26px;top:-22px}
.rating{display:flex;align-items:center;gap:2px}
.rating i{width:17px;height:17px;background:var(--green);display:block}
.verified{margin-left:9px;font-size:12.5px;color:#666;display:flex;align-items:center;gap:4px}
.review-text{font-style:italic;font-size:12.5px;line-height:17.5px;color:#333;margin-top:21px;height:94px}
.reviewer{font-family:'Roboto',sans-serif;font-weight:700;font-size:16.5px;color:#111}
.pager{left:573px;top:2077px;display:flex;gap:12px;align-items:center}
.pager i{width:9px;height:9px;border-radius:50%;background:#ddd;display:block}
.pager i.on{background:var(--deep-red)}

/* footer */
.site-footer{position:absolute;left:0;top:2645px;width:1200px;height:339px;background:var(--ink);color:#aaa}
.footer-badge{left:135px;top:88px;width:128px;height:128px;border-radius:50%;background:#fff;display:flex;align-items:center;justify-content:center;text-align:center;font-weight:700;font-size:16px;line-height:1.2;color:var(--ink)}
.footer-col h4{font-size:13.5px;font-weight:700;color:#fff;margin-bottom:14px}
.footer-col a{display:block;font-size:10.5px;color:#aaa;text-decoration:none;line-height:22.6px}
.contact-line{display:flex;gap:8px;font-size:10.5px;line-height:13px;margin-bottom:16px;color:#aaa}
.footer-rule{left:135px;top:279px;width:930px;height:1px;background:#3a3940}
.copyright{left:135px;top:303px;font-size:10px;color:#ccc}
.payments{left:859px;top:297px;display:flex;gap:9px}
.payments i{width:35px;height:22px;border-radius:3px;background:#fff;display:block}
</style>
</head>
<body>

<header class="site-header">
  <div class="abs menu-icon"><span></span><span></span><span></span></div>
  <svg class="abs search-icon" width="16" height="16" viewBox="0 0 16 16"><circle cx="6.5" cy="6.5" r="5" fill="none" stroke="#444" stroke-width="2"/><path d="M10 10l5 5" stroke="#444" stroke-width="2"/></svg>
  <div class="abs sign-in">SIGN IN / REGISTER</div>
  <svg class="abs cart-icon" width="22" height="24" viewBox="0 0 22 24"><path d="M2 8h18l-1.5 15h-15z" fill="none" stroke="#fff" stroke-width="1.6"/><path d="M7 8V5a4 4 0 0 1 8 0v3" fill="none" stroke="#fff" stroke-width="1.6"/></svg>
  <div class="abs cart-count">2</div>
  <div class="abs cart-label">MY CART</div>
  <div class="abs cart-total">£119.00</div>
</header>
<div class="abs brand-badge">Crooked<br>Thrill</div>

<section class="hero">
  <div class="hero-photo" role="img" aria-label="Four friends wearing white brand t-shirts and dark trousers against a light grey wall"></div>
</section>
<div class="abs deal-kicker">DEALS OF DAY</div>
<h1 class="abs deal-title">SKATE BOARD</h1>
<div class="abs deal-price">$225.00</div>
<div class="abs deal-bought">
  <svg width="32" height="26" viewBox="0 0 32 26"><circle cx="16" cy="6" r="5" fill="#222"/><circle cx="6" cy="9" r="4" fill="#222"/><circle cx="26" cy="9" r="4" fill="#222"/><path d="M7 26c0-7 4-12 9-12s9 5 9 12z" fill="#222"/><path d="M0 24c0-5 3-9 6-9s4 2 4 2l-3 7z" fill="#222"/><path d="M32 24c0-5-3-9-6-9s-4 2-4 2l3 7z" fill="#222"/></svg>
  20 BOUGHT
</div>
<div class="abs countdown">
  <div class="count-box"><b>03</b><span>DAYS</span></div>
  <div class="count-box"><b>15</b><span>HOURS</span></div>
  <div class="count-box"><b>29</b><span>MINS</span></div>
  <div class="count-box"><b>58</b><span>SECS</span></div>
</div>
<div class="abs btn-accent shop-now">SHOP NOW</div>
<div class="abs btn-accent view-details">VIEW DETAILS</div>

<p class="abs about">Founded in the heart of the urban jungle, Crooked Thrill is more than just a brand—it's a movement. Inspired by the raw energy of skate parks, the thrill of BMX trails, the freedom of the open road, and the spirit of rebellion, our mission is to provide high-quality gear for those who live life on the edge. Join us in celebrating individuality, adventure, and the relentless pursuit of excitement.</p>

<h2 class="abs section-title" style="left:111px;top:826px">OTHER DEALS</h2>
<div class="abs carousel-arrow arrow-left" style="left:34px;top:1003px"><svg width="10" height="14"><path d="M8 1L2 7l6 6" fill="none" stroke="#fff" stroke-width="2"/></svg></div>
<div class="abs carousel-arrow arrow-right" style="left:1131px;top:1003px"><svg width="10" height="14"><path d="M2 1l6 6-6 6" fill="none" stroke="#fff" stroke-width="2"/></svg></div>

<div class="abs product-row" style="top:892px">
  <article class="product-card">
    <div class="product-image" role="img" aria-label="Black cruiser motorcycle parked on a street" style="background:linear-gradient(160deg,#9a9c9e,#2b2b2d 60%,#6d6f70)"></div>
    <h3 class="product-name" style="font-weight:400">Rebel Rider</h3>
    <p class="product-specs">Material: 7-ply Canadian maple<br>Dimensions: 8.25" x 32.5"<br>Concave: Medium</p>
    <div class="product-price"><s>$225</s><b>$175</b><span class="likes"><svg width="11" height="10"><path d="M0 4h2v6H0zM3 4l3-4c1 0 1.5.5 1.3 1.6L7 4h3.2c.6 0 .9.5.8 1L10 9.3c-.1.4-.5.7-.9.7H3z" fill="#999"/></svg>32</span></div>
    <p class="free-ship">+ Free Shipping</p>
    <div class="detail-btn">VIEW DETAIL</div>
  </article>
  <article class="product-card">
    <div class="product-image" role="img" aria-label="Black skateboard deck with orange wheels on a white background" style="background:radial-gradient(ellipse at 50% 50%,#3a3a3a 0%,#6e6e6e 28%,#e9e9ea 45%)"></div>
    <h3 class="product-name" style="font-weight:400">Skate Board</h3>
    <p class="product-specs">Material: 7-ply Canadian maple<br>Dimensions: 8.25" x 32.5"<br>Concave: Medium</p>
    <div class="product-price"><s>$225</s><b>$175</b><span class="likes"><svg width="11" height="10"><path d="M0 4h2v6H0zM3 4l3-4c1 0 1.5.5 1.3 1.6L7 4h3.2c.6 0 .9.5.8 1L10 9.3c-.1.4-.5.7-.9.7H3z" fill="#999"/></svg>32</span></div>
    <p class="free-ship">+ Free Shipping</p>
    <div class="detail-btn">VIEW DETAIL</div>
  </article>
  <article class="product-card">
    <div class="product-image" role="img" aria-label="Surfboard standing in beach sand under palm trees" style="background:linear-gradient(180deg,#3f8fc4 0%,#6fb0d6 45%,#d8c7a6 75%,#c7b08a 100%)"></div>
    <h3 class="product-name" style="font-weight:400">Surfing</h3>
    <p class="product-specs">Material: 7-ply Canadian maple<br>Dimensions: 8.25" x 32.5"<br>Concave: Medium</p>
    <div class="product-price"><s>$225</s><b>$175</b><span class="likes"><svg width="11" height="10"><path d="M0 4h2v6H0zM3 4l3-4c1 0 1.5.5 1.3 1.6L7 4h3.2c.6 0 .9.5.8 1L10 9.3c-.1.4-.5.7-.9.7H3z" fill="#999"/></svg>32</span></div>
    <p class="free-ship">+ Free Shipping</p>
    <div class="detail-btn">VIEW DETAIL</div>
  </article>
  <article class="product-card">
    <div class="product-image" role="img" aria-label="Skater in a yellow jacket lacing up inline skates" style="background:linear-gradient(170deg,#c9a21a 0%,#8b7a5a 30%,#4c5260 60%,#7a6a55 100%)"></div>
    <h3 class="product-name" style="font-weight:400">Skate</h3>
    <p class="product-specs">Material: 7-ply Canadian maple<br>Dimensions: 8.25" x 32.5"<br>Concave: Medium</p>
    <div class="product-price"><s>$225</s><b>$175</b><span class="likes"><svg width="11" height="10"><path d="M0 4h2v6H0zM3 4l3-4c1 0 1.5.5 1.3 1.6L7 4h3.2c.6 0 .9.5.8 1L10 9.3c-.1.4-.5.7-.9.7H3z" fill="#999"/></svg>32</span></div>
    <p class="free-ship">+ Free Shipping</p>
    <div class="detail-btn">VIEW DETAIL</div>
  </article>
  <article class="product-card">
    <div class="product-image" role="img" aria-label="Tattooed man portrait against a dark background" style="background:linear-gradient(180deg,#3e3e42 0%,#6a5a52 45%,#3a3c4a 100%)"></div>
    <h3 class="product-name" style="font-weight:400">Tattoos</h3>
    <p class="product-specs">Material: 7-ply Canadian maple<br>Dimensions: 8.25" x 32.5"<br>Concave: Medium</p>
    <div class="product-price"><s>$225</s><b>$175</b><span class="likes"><svg width="11" height="10"><path d="M0 4h2v6H0zM3 4l3-4c1 0 1.5.5 1.3 1.6L7 4h3.2c.6 0 .9.5.8 1L10 9.3c-.1.4-.5.7-.9.7H3z" fill="#999"/></svg>32</span></div>
    <p class="free-ship">+ Free Shipping</p>
    <div class="detail-btn">VIEW DETAIL</div>
  </article>
</div>

<section class="signup">
  <div class="signup-arc"></div>
  <svg class="dot-grid" width="130" height="160" viewBox="0 0 130 160">
    <defs><pattern id="dots" width="15" height="15" patternUnits="userSpaceOnUse"><circle cx="4" cy="4" r="2.5" fill="rgba(255,255,255,.25)"/></pattern></defs>
    <rect width="130" height="160" fill="url(#dots)"/>
  </svg>
  <h2>SIGN UP FOR NEWS &amp; GET 25% OFF!</h2>
  <p>EXCLUSIVE OFFER FOR NEW MEMBER! SIGN UP TO DAY!</p>
  <div class="signup-form"><div class="email-field">EMAIL...</div><div class="subscribe">SUBSCRIBE</div></div>
</section>

<h2 class="abs section-title" style="left:0;width:1200px;text-align:center;top:1716px">CUSTOMERS REVIEWS</h2>

<div class="review-card" style="left:133px">
  <svg class="review-quote" width="42" height="34" viewBox="0 0 42 34"><path d="M0 34V18C0 8 5 2 15 0l2 4C11 6 9 10 9 15h8v19zM25 34V18c0-10 5-16 15-18l2 4c-6 2-8 6-8 11h8v19z" fill="#8a8a8a"/></svg>
  <div class="rating"><i></i><i></i><i></i><i></i><i></i><span class="verified"><svg width="13" height="13"><circle cx="6.5" cy="6.5" r="6.5" fill="#777"/><path d="M3.5 6.5l2 2 4-4" fill="none" stroke="#fff" stroke-width="1.5"/></svg>Verified</span></div>
  <p class="review-text">“The surfboard I purchased exceeded my expectations. It's lightweight, sturdy, and the design is awesome. It definitely turns heads at the beach.”</p>
  <p class="reviewer">-Lisa S., Surfer</p>
</div>
<div class="review-card" style="left:455px">
  <svg class="review-quote" width="42" height="34" viewBox="0 0 42 34"><path d="M0 34V18C0 8 5 2 15 0l2 4C11 6 9 10 9 15h8v19zM25 34V18c0-10 5-16 15-18l2 4c-6 2-8 6-8 11h8v19z" fill="#8a8a8a"/></svg>
  <div class="rating"><i></i><i></i><i></i><i></i><i></i><span class="verified"><svg width="13" height="13"><circle cx="6.5" cy="6.5" r="6.5" fill="#777"/><path d="M3.5 6.5l2 2 4-4" fill="none" stroke="#fff" stroke-width="1.5"/></svg>Verified</span></div>
  <p class="review-text">“The 'Rebel Rider' skateboard deck is amazing! The quality is top-notch, and it rides so smoothly. The graphics are even better in person. Highly recom-mend!”</p>
  <p class="reviewer">-Mark D., Motorcycle</p>
</div>
<div class="review-card" style="left:774px">
  <svg class="review-quote" width="42" height="34" viewBox="0 0 42 34"><path d="M0 34V18C0 8 5 2 15 0l2 4C11 6 9 10 9 15h8v19zM25 34V18c0-10 5-16 15-18l2 4c-6 2-8 6-8 11h8v19z" fill="#8a8a8a"/></svg>
  <div class="rating"><i></i><i></i><i></i><i></i><i></i><span class="verified"><svg width="13" height="13"><circle cx="6.5" cy="6.5" r="6.5" fill="#777"/><path d="M3.5 6.5l2 2 4-4" fill="none" stroke="#fff" stroke-width="1.5"/></svg>Verified</span></div>
  <p class="review-text">“I bought the leather jacket and it’s become my go-to for every ride. It’s durable, stylish, and the fit is perfect. Can’t wait to see what else you come out with!”</p>
  <p class="reviewer">-Kevin R., BMX Rider</p>
</div>
<div class="abs pager"><i></i><i class="on"></i><i></i></div>

<h2 class="abs section-title" style="left:111px;top:2146px">FEATURE PRODUCTS</h2>
<div class="abs carousel-arrow arrow-left" style="left:34px;top:2323px"><svg width="10" height="14"><path d="M8 1L2 7l6 6" fill="none" stroke="#fff" stroke-width="2"/></svg></div>
<div class="abs carousel-arrow arrow-right" style="left:1131px;top:2323px"><svg width="10" height="14"><path d="M2 1l6 6-6 6" fill="none" stroke="#fff" stroke-width="2"/></svg></div>

<div class="abs product-row" style="top:2212px">
  <article class="product-card">
    <div class="product-image" role="img" aria-label="Colourful graphic skateboard deck on a light grey background" style="background:radial-gradient(ellipse at 50% 55%,#4a5fb0 0%,#8a7ac0 22%,#e6e6e8 48%)"></div>
    <h3 class="product-name" style="font-weight:400">Skate</h3>
    <p class="product-specs">Material: 7-ply Canadian maple<br>Dimensions: 8.25" x 32.5"<br>Concave: Medium</p>
    <div class="product-price"><s>$225</s><b>$175</b><span class="likes"><svg width="11" height="10"><path d="M0 4h2v6H0zM3 4l3-4c1 0 1.5.5 1.3 1.6L7 4h3.2c.6 0 .9.5.8 1L10 9.3c-.1.4-.5.7-.9.7H3z" fill="#999"/></svg>32</span></div>
    <p class="free-ship">+ Free Shipping</p>
    <div class="detail-btn">VIEW DETAIL</div>
  </article>
  <article class="product-card">
    <div class="product-image" role="img" aria-label="Sunburst electric guitar on a stand" style="background:radial-gradient(ellipse at 55% 65%,#7a1b12 0%,#2a1a16 20%,#c7c7c9 45%,#dedede 100%)"></div>
    <h3 class="product-name" style="font-weight:400">Rock n Roll</h3>
    <p class="product-specs">Material: 7-ply Canadian maple<br>Dimensions: 8.25" x 32.5"<br>Concave: Medium</p>
    <div class="product-price"><s>$225</s><b>$175</b><span class="likes"><svg width="11" height="10"><path d="M0 4h2v6H0zM3 4l3-4c1 0 1.5.5 1.3 1.6L7 4h3.2c.6 0 .9.5.8 1L10 9.3c-.1.4-.5.7-.9.7H3z" fill="#999"/></svg>32</span></div>
    <p class="free-ship">+ Free Shipping</p>
    <div class="detail-btn">VIEW DETAIL</div>
  </article>
  <article class="product-card">
    <div class="product-image" role="img" aria-label="Black motorcycle on a white background" style="background:radial-gradient(ellipse at 50% 55%,#2a2a2c 0%,#55565a 25%,#eeeeef 50%)"></div>
    <h3 class="product-name" style="font-weight:400">Motorcycle</h3>
    <p class="product-specs">Material: 7-ply Canadian maple<br>Dimensions: 8.25" x 32.5"<br>Concave: Medium</p>
    <div class="product-price"><s>$225</s><b>$175</b><span class="likes"><svg width="11" height="10"><path d="M0 4h2v6H0zM3 4l3-4c1 0 1.5.5 1.3 1.6L7 4h3.2c.6 0 .9.5.8 1L10 9.3c-.1.4-.5.7-.9.7H3z" fill="#999"/></svg>32</span></div>
    <p class="free-ship">+ Free Shipping</p>
    <div class="detail-btn">VIEW DETAIL</div>
  </article>
  <article class="product-card">
    <div class="product-image" role="img" aria-label="Tattooed forearms and hands against a light blue shirt" style="background:linear-gradient(180deg,#9ab8d6 0%,#c49a85 50%,#8fb0cf 100%)"></div>
    <h3 class="product-name" style="font-weight:400">Tattoos</h3>
    <p class="product-specs">Material: 7-ply Canadian maple<br>Dimensions: 8.25" x 32.5"<br>Concave: Medium</p>
    <div class="product-price"><s>$225</s><b>$175</b><span class="likes"><svg width="11" height="10"><path d="M0 4h2v6H0zM3 4l3-4c1 0 1.5.5 1.3 1.6L7 4h3.2c.6 0 .9.5.8 1L10 9.3c-.1.4-.5.7-.9.7H3z" fill="#999"/></svg>32</span></div>
    <p class="free-ship">+ Free Shipping</p>
    <div class="detail-btn">VIEW DETAIL</div>
  </article>
  <article class="product-card">
    <div class="product-image" role="img" aria-label="Rider in black standing beside a black motorcycle" style="background:linear-gradient(180deg,#d4d4d4 0%,#7a7a7a 50%,#2c2c2e 80%,#bdbdbd 100%)"></div>
    <h3 class="product-name" style="font-weight:400">Rebel Rider</h3>
    <p class="product-specs">Material: 7-ply Canadian maple<br>Dimensions: 8.25" x 32.5"<br>Concave: Medium</p>
    <div class="product-price"><s>$225</s><b>$175</b><span class="likes"><svg width="11" height="10"><path d="M0 4h2v6H0zM3 4l3-4c1 0 1.5.5 1.3 1.6L7 4h3.2c.6 0 .9.5.8 1L10 9.3c-.1.4-.5.7-.9.7H3z" fill="#999"/></svg>32</span></div>
    <p class="free-ship">+ Free Shipping</p>
    <div class="detail-btn">VIEW DETAIL</div>
  </article>
</div>

<footer class="site-footer">
  <div class="abs footer-badge">Crooked<br>Thrill</div>
  <div class="abs footer-col" style="left:360px;top:98px"><h4>ABOUT</h4><a>About Us</a><a>Shopping Guide</a><a>Delivery Information</a><a>Privacy Policy</a><a>Sitemap</a></div>
  <div class="abs footer-col" style="left:549px;top:98px"><h4>ACCOUNT</h4><a>My Account</a><a>Wishlist</a><a>Order Tracking</a><a>Shipping Info</a><a>Return Policy</a></div>
  <div class="abs footer-col" style="left:703px;top:98px"><h4>MERCHANTS</h4><a>Run a Deal</a><a>Merchant Centre</a><a>Newsletter Signup</a></div>
  <div class="abs footer-col" style="left:871px;top:98px">
    <h4>Contact Us</h4>
    <div class="contact-line" style="margin-top:18px"><svg width="11" height="9"><rect x=".5" y=".5" width="10" height="8" fill="none" stroke="#fff"/><path d="M.5.5l5 4 5-4" fill="none" stroke="#fff"/></svg>hello@crookedthrill.shop</div>
    <div class="contact-line"><svg width="11" height="11"><path d="M2 0l2 3-1.2 1.5a7 7 0 0 0 3.7 3.7L8 7l3 2-1 2C5 11 0 6 0 1z" fill="#fff"/></svg>(555) 010-2468</div>
    <div class="contact-line"><svg width="9" height="12"><path d="M4.5 0A4.5 4.5 0 0 1 9 4.5C9 8 4.5 12 4.5 12S0 8 0 4.5A4.5 4.5 0 0 1 4.5 0z" fill="#fff"/><circle cx="4.5" cy="4.5" r="1.7" fill="#1f1e25"/></svg><span>27 Gravel Lane, Dockside Row,<br>Harbor City</span></div>
  </div>
  <div class="abs footer-rule"></div>
  <div class="abs copyright">COPYRIGHT 2024 CROOKEDTHRILL-ALL RIGHT RESERVED</div>
  <div class="abs payments" aria-label="Accepted payment methods"><i></i><i></i><i></i><i></i><i></i></div>
</footer>

</body>
</html>
```